New website for a commercial real estate consulting company

What we’re looking for in a new web site:
• Desktop and mobile friendly
• Clear navigation
• Strong graphics
• Professional appearance
• The ability to update it ourselves
• Site is for information purposes only – no transactions required
• Traffic counts – number of visits per page?
• A firm quote on costs to develop and launch
• SSL
Attached is a copy of the revised text we propose to use, including our new logo. (The pagination can be different than as shown.)
Our current website address is www.tamblinvaleadvisory.ca

```html
<!DOCTYPE html>
<html lang="en">
<head>
<meta charset="utf-8">
<title>Tamblin Vale Advisory</title>
<link href="https://fonts.googleapis.com/css2?family=Lato:wght@300;400;700&display=swap" rel="stylesheet">
<style>
:root{
  --navy:#1c2b8f;
  --navy-deep:#0f1a5c;
  --ink:#1b1b1b;
  --muted:#6a6a6a;
  --light:#f4f4f4;
  --yellow:#f3dc1a;
  --white:#ffffff;
}
*{margin:0;padding:0;box-sizing:border-box}
html,body{width:1200px;height:1200px;overflow:hidden;background:var(--white);font-family:'Lato',sans-serif;color:var(--ink)}
.stage{position:absolute;left:0;top:0;width:1500px;height:1500px;transform:scale(.8);transform-origin:0 0}
.page{position:absolute;left:464px;top:0;width:574px;height:1500px;background:var(--white)}
.abs{position:absolute}
.h-title{font-size:8px;font-weight:700;letter-spacing:.2px;color:var(--ink)}
.h-title::after{content:"";display:block;width:22px;height:1.5px;background:var(--navy);margin-top:5px}
.small{font-size:4.6px;line-height:10px;color:#444}

/* hero */
.hero{left:0;top:0;width:574px;height:282px;background:linear-gradient(120deg,#243aa6 0%,#1c2b8f 60%,#1a2a86 100%)}
.hero-photo{left:0;top:0;width:206px;height:282px;background:linear-gradient(180deg,#2a2a2a,#161616 70%,#0e0e0e)}
.brand{left:96px;top:12px;width:86px;text-align:center;color:#d8d8d8;font-size:6px;letter-spacing:1.2px;white-space:nowrap}
.brand .sq{display:block;width:9px;height:9px;background:var(--navy);margin:0 auto 5px}
.nav{top:26px;left:242px;display:flex;gap:16px;font-size:5.5px;color:var(--white);white-space:nowrap}
.nav .active{border-bottom:1px solid var(--white);padding-bottom:2px}
.call{left:430px;top:22px;width:73px;height:15px;border:1px solid var(--white);color:var(--yellow);font-size:5.5px;display:flex;align-items:center;justify-content:center;white-space:nowrap}
.hero-head{left:238px;top:94px;width:180px;color:var(--white);font-size:8px;line-height:13px;font-weight:400}
.hero-sub{left:238px;top:122px;width:130px;color:#dfe3ff;font-size:4.6px;line-height:8px}
.hero-line{left:182px;top:152px;width:47px;height:1px;background:var(--white)}
.hero-more{left:238px;top:148px;color:var(--white);font-size:6px}
.hero-arrows{left:160px;top:201px;width:90px;height:22px;background:linear-gradient(90deg,rgba(255,255,255,0),rgba(255,255,255,.18),rgba(255,255,255,0))}
.hero-building{left:350px;top:100px;width:224px;height:182px;background:radial-gradient(ellipse at 70% 70%,rgba(214,222,236,.85),rgba(120,135,175,.45) 55%,rgba(28,43,143,0) 80%)}

/* about */
.about{left:0;top:282px;width:574px;height:233px;background:var(--light)}
.about .h-title{left:72px;top:64px}
.about .small{left:72px;top:88px;width:232px}
.btn{left:72px;top:150px;width:65px;height:18px;background:var(--navy);color:var(--white);font-size:5.5px;display:flex;align-items:center;justify-content:center;gap:4px}
.about-ring{left:340px;top:48px;width:160px;height:140px;border-radius:50%;background:radial-gradient(circle at 40% 50%,#fff 55%,#ececec 72%,rgba(244,244,244,0) 74%)}
.about-art{left:352px;top:78px;width:118px;height:80px;border-radius:6px;background:linear-gradient(160deg,#d7dcd6,#e9e1cc 60%,#f2f0ea)}

/* services */
.svc .h-title{left:260px;top:544px}
.svc .small{left:260px;top:568px;width:196px}
.city{left:80px;top:790px;width:420px;height:118px;background:linear-gradient(180deg,rgba(210,240,240,0),rgba(200,232,236,.55));border-bottom:1px solid #eee}
.ring{width:106px;height:106px;border-radius:50%;background:var(--white);box-shadow:0 0 10px rgba(0,0,0,.12);display:flex;align-items:center;justify-content:center}
.ring .img{width:84px;height:84px;border-radius:50%}
.svc-label{font-size:6.5px;font-weight:700;color:var(--ink);white-space:nowrap}

/* profile */
.profile .h-title{left:260px;top:938px}
.wedge{left:0;top:948px;width:274px;height:218px}
.portrait{left:155px;top:1008px;width:119px;height:158px;background:linear-gradient(180deg,#a3a3a3 0%,#9a8f8f 30%,#c8252e 48%,#b81f28 100%)}
.bio-name{left:302px;top:998px;font-size:8.5px;font-weight:700;color:var(--navy);white-space:nowrap}
.bio-mail{left:302px;top:1011px;font-size:4.5px;color:#999}
.bio-rule{left:293px;top:1018px;width:1px;height:148px;background:#ccc}
.bio-text{left:302px;top:1026px;width:196px}
.bullet{left:302px;width:190px;display:flex;gap:5px}
.bullet i{flex:none;width:7px;height:7px;border:1px solid var(--navy);border-radius:50%;position:relative;margin-top:1px}
.bullet i::after{content:"";position:absolute;left:1.5px;top:1.5px;width:2px;height:2px;border-radius:50%;background:var(--navy)}

/* events */
.events{left:0;top:1187px;width:574px;height:188px;background:linear-gradient(160deg,#2d45b0,#1c2b8f 50%,#233aa0)}
.events .h-title{left:0;width:574px;top:28px;text-align:center;color:var(--white);font-weight:400}
.events .h-title::after{margin:5px auto 0;background:var(--white)}
.date{width:32px;height:32px;border-radius:50%;background:var(--yellow);box-shadow:0 0 0 2px var(--navy-deep),0 0 0 3px var(--yellow);display:flex;align-items:center;justify-content:center;text-align:center;font-size:4.3px;line-height:6px;color:var(--navy-deep)}
.ev{font-size:5px;line-height:8px;font-weight:700;color:var(--white);white-space:nowrap}

/* footer */
.f-brand{left:62px;top:1400px;width:80px;text-align:center}
.f-brand .sq{display:block;width:12px;height:12px;background:var(--navy);margin:0 auto 12px}
.f-brand .name{font-size:5px;letter-spacing:1px;color:var(--navy);white-space:nowrap}
.f-brand .who{font-size:5.5px;font-weight:700;color:var(--navy);margin-top:6px;white-space:nowrap}
.f-item{top:1406px;text-align:center;font-size:5px;line-height:8px;color:var(--navy)}
.f-item svg{display:block;margin:0 auto 8px}
.f-rule{left:0;top:1480px;width:574px;height:1px;background:#e6e6e6}
.copy{left:0;width:574px;top:1486px;text-align:center;font-size:5px;color:#777}
</style>
</head>
<body>
<div class="stage">
<main class="page">

  <section class="abs hero">
    <div class="abs hero-photo" role="img" aria-label="Dark photograph of a high-rise building silhouette"></div>
    <div class="abs brand"><span class="sq"></span>TAMBLIN VALE</div>
    <nav class="abs nav"><span class="active">Home</span><span>About us</span><span>Who we are</span><span>Contact us</span></nav>
    <div class="abs call">Call : 905.555.0148</div>
    <h1 class="abs hero-head">Tamblin Vale Advisory is an independent consulting firm offering practical</h1>
    <p class="abs hero-sub">There are many variations of passages of Lorem Ipsum available, but the majority</p>
    <div class="abs hero-line"></div>
    <div class="abs hero-more">Read More</div>
    <div class="abs hero-arrows">
      <svg width="90" height="22" viewBox="0 0 90 22"><g stroke="#fff" stroke-width=".8" fill="none"><path d="M4 11h8M4 11l3-3M4 11l3 3"/><path d="M18 11h8M26 11l-3-3M26 11l-3 3"/></g></svg>
    </div>
    <div class="abs hero-building" role="img" aria-label="Photograph of a modern apartment tower with balconies"></div>
  </section>

  <section class="abs about">
    <h2 class="abs h-title">ABOUT US</h2>
    <p class="abs small">Tamblin Vale Advisory is an independent consulting firm offering practical, hands-on assistance to the commercial real estate and commercial mortgage lending industries. We specialize in financial analysis, underwriting and financial due diligence. Working with us, you get top notch help when you need it – and only when you need it – one project at a time.</p>
    <div class="abs btn">Read More <svg width="8" height="5" viewBox="0 0 8 5"><path d="M0 2.5h7M5 .5l2 2-2 2" stroke="#fff" stroke-width=".7" fill="none"/></svg></div>
    <div class="abs about-ring"></div>
    <div class="abs about-art" role="img" aria-label="Illustration of a two-storey suburban house"></div>
  </section>

  <section class="svc">
    <h2 class="abs h-title">WHAT WE DO</h2>
    <p class="abs small">The foundation of our success has been our commitment to exceeding our clients' expectations, both in quality and in timeliness. We strive to go above and beyond on every assignment.</p>
    <div class="abs city" role="img" aria-label="Faint illustration of a city skyline"></div>

    <div class="abs ring" style="left:227px;top:623px"><div class="img" role="img" aria-label="Photo of hands joined over documents" style="background:linear-gradient(135deg,#d9b59c,#eef0f2 60%,#c9ccd2)"></div></div>
    <div class="abs ring" style="left:157px;top:699px"><div class="img" style="background:#2f3aa8;display:flex;align-items:center;justify-content:center"><svg width="12" height="8" viewBox="0 0 12 8"><path d="M0 4h11M8 1l3 3-3 3" stroke="#fff" stroke-width=".8" fill="none"/></svg></div></div>
    <div class="abs ring" style="left:297px;top:699px"><div class="img" role="img" aria-label="Photo of a hand dropping a coin into a jar" style="background:linear-gradient(135deg,#f1f1f1,#dcd3c7 70%,#c9a88a)"></div></div>
    <div class="abs ring" style="left:227px;top:775px"><div class="img" role="img" aria-label="Photo of a couple holding a sale sign" style="background:linear-gradient(180deg,#4aa4e0,#2b7fc2 55%,#c25a35)"></div></div>

    <svg class="abs" style="left:0;top:600px" width="574" height="290" viewBox="0 0 574 290">
      <g stroke="#1c2b8f" stroke-width="1.6" fill="none" stroke-linecap="round">
        <path d="M320 38c5-10 15-12 24-8"/><path d="M340 26l4 4-5 3"/>
        <path d="M184 105c-2-10-14-16-32-15"/><path d="M156 86l-4 4 5 3"/>
        <path d="M396 182c4 11 15 14 30 12"/><path d="M422 190l4 4-4 4"/>
        <path d="M236 258c-4 12-18 15-32 12"/><path d="M208 266l-4 4 5 3"/>
      </g>
    </svg>
    <div class="abs svc-label" style="left:357px;top:630px">For Buyers</div>
    <div class="abs svc-label" style="left:101px;top:688px">For Owners</div>
    <div class="abs svc-label" style="left:433px;top:788px">For Lenders</div>
    <div class="abs svc-label" style="left:153px;top:866px">For Brokers</div>
  </section>

  <section class="profile">
    <h2 class="abs h-title">WHAT WE DO</h2>
    <svg class="abs wedge" viewBox="0 0 274 218" width="274" height="218">
      <defs><linearGradient id="wedgeFill" x1="0" y1="0" x2="1" y2="1"><stop offset="0" stop-color="#12183a"/><stop offset="1" stop-color="#1c2b8f"/></linearGradient></defs>
      <polygon points="0,0 274,170 274,218 0,218" fill="url(#wedgeFill)"/>
    </svg>
    <div class="abs portrait" role="img" aria-label="Portrait photo of the principal consultant in a red jacket"></div>
    <div class="abs bio-name">Marian Ostrowe, MBA, MRICS</div>
    <div class="abs bio-mail">marian.ostrowe@tamblinvaleadvisory.ca</div>
    <div class="abs bio-rule"></div>
    <p class="abs small bio-text" style="line-height:9px">Marian has more than 30 years' senior experience in a wide range of property types. Her expertise encompasses all aspects of the financing, valuation, purchase and sale of commercial real estate. Prior to founding Tamblin Vale Advisory in 2001, Marian spent 16 years of her career in a variety of institutional roles, culminating in ten years as Vice-President, Property Investments of a Canadian life insurance company. Working in a leadership capacity, Marian's career also includes:</p>
    <div class="abs bullet small" style="top:1098px;line-height:9px"><i></i><span>Acquisitions, dispositions, and asset management for a life company's equity real estate portfolio.</span></div>
    <div class="abs bullet small" style="top:1123px;line-height:9px"><i></i><span>Roles on both the buy and the sell sides of a corporate sale: on the due diligence team for two potential purchases of life insurance companies; key member of the selling team for a life insurance company.</span></div>
    <div class="abs bullet small" style="top:1158px;line-height:9px"><i></i><span>Corporate secretary of a life insurance company for five years.</span></div>
  </section>

  <section class="abs events" role="group" aria-label="Industry events calendar">
    <h2 class="abs h-title">INDUSTRY EVENTS CALENDAR</h2>
    <div class="abs date" style="left:86px;top:69px">January<br>2019</div>
    <div class="abs ev" style="left:126px;top:81px">27-29 CRE SUMMIT</div>
    <div class="abs date" style="left:209px;top:69px">February<br>2019</div>
    <div class="abs ev" style="left:251px;top:81px">26 CAPITAL FORUM</div>
    <div class="abs date" style="left:379px;top:69px">March<br>2019</div>
    <div class="abs ev" style="left:420px;top:76px">6 WOMEN IN PROPERTY AGM<br>27 PM SPRINGFEST</div>
    <div class="abs date" style="left:86px;top:124px">April<br>2019</div>
    <div class="abs ev" style="left:126px;top:132px">3 OWNERS FORUM AGM<br>9 REALTY MERIT GALA</div>
    <div class="abs date" style="left:209px;top:124px">May<br>2019</div>
    <div class="abs ev" style="left:251px;top:132px">22 BUILDING MERIT GALA<br>29 LAND &amp; DEVELOPMENT CONFERENCE</div>
    <div class="abs date" style="left:379px;top:124px">June<br>2019</div>
    <div class="abs ev" style="left:420px;top:131px">6 WOMEN IN PROPERTY AGM<br>27 PM SPRINGFEST</div>
  </section>

  <footer>
    <div class="abs f-brand"><span class="sq"></span><div class="name">TAMBLIN VALE</div><div class="who">MARIAN OSTROWE</div></div>
    <div class="abs f-item" style="left:170px;width:40px">
      <svg width="16" height="16" viewBox="0 0 16 16"><circle cx="8" cy="8" r="7.3" fill="none" stroke="#1c2b8f" stroke-width=".7"/><path d="M5.5 4.5l1.5 1.5-1 1c.6 1.3 1.5 2.2 2.8 2.8l1-1 1.5 1.5-1 1c-2.8-.5-5.3-3-5.8-5.8z" fill="none" stroke="#1c2b8f" stroke-width=".6"/></svg>905.555.0148</div>
    <div class="abs f-item" style="left:232px;width:40px">
      <svg width="16" height="16" viewBox="0 0 16 16"><circle cx="8" cy="8" r="7.3" fill="none" stroke="#1c2b8f" stroke-width=".7"/><rect x="5.8" y="4" width="4.4" height="8" rx=".8" fill="none" stroke="#1c2b8f" stroke-width=".6"/></svg>905.555.0148</div>
    <div class="abs f-item" style="left:270px;width:140px">
      <svg width="16" height="16" viewBox="0 0 16 16"><circle cx="8" cy="8" r="7.3" fill="none" stroke="#1c2b8f" stroke-width=".7"/><rect x="4.5" y="5.5" width="7" height="5" fill="none" stroke="#1c2b8f" stroke-width=".6"/><path d="M4.5 5.5L8 8.3l3.5-2.8" fill="none" stroke="#1c2b8f" stroke-width=".6"/></svg>marian.ostrowe@tamblinvaleadvisory.ca</div>
    <div class="abs f-item" style="left:436px;width:90px;text-align:left">
      <svg width="16" height="16" viewBox="0 0 16 16" style="margin:0 0 8px 2px"><circle cx="8" cy="8" r="7.3" fill="none" stroke="#1c2b8f" stroke-width=".7"/><path d="M8 12.2s3-3.2 3-5.2a3 3 0 00-6 0c0 2 3 5.2 3 5.2z" fill="none" stroke="#1c2b8f" stroke-width=".6"/><circle cx="8" cy="7" r="1" fill="none" stroke="#1c2b8f" stroke-width=".6"/></svg>Tamblin Vale Advisory<br>84 Fennick Street<br>Acton, Ontario L0P 2K4</div>
    <div class="abs f-rule"></div>
    <div class="abs copy">@Tamblinvaleadvisory 2019</div>
  </footer>

</main>
</div>
</body>
</html>
```